Book cover design for modern bagpipe music book

This music book will be A4 in size and requires a design for the front and back cover. The focus is on creating a modern and eye catching design, breaking away from the stereotypes of what people think of when they think of bagpipes. Think the OPPOSITE of a bagpiper in a full kilt standing on top of a mountain playing Lanterns on the Moor!

Book title: Wake Stroll Hum Again

Other front cover text : Music for the bagpipes by Dara Colby

Front cover file ideas uploaded

2 pictures of bagpipes attached.

- The real set of bagpipes give an idea of the correct finer details

- The toy bagpipes perhaps have a better shape with the left 'stick' down

Back cover - No real brief. Keen for it not to be a full block single colour though.

Design requires 3mm bleed for print

Open to ideas and suggestions! Thank you!

```html
<!DOCTYPE html>
<html lang="en">
<head>
<meta charset="utf-8">
<title>Wake Stroll Hum Again – Cover Spread</title>
<link href="https://fonts.googleapis.com/css2?family=Bebas+Neue&family=Montserrat:wght@300;400;800&display=swap" rel="stylesheet">
<style>
  :root {
    --stage: #6f6f6f;
    --tartan-deep: #2a0d0f;
    --tartan-red: #7a1a1e;
    --tartan-bright: #a8262b;
    --tartan-green: #2c3a2f;
    --gold-dark: #a8751f;
    --gold: #d9a63a;
    --gold-light: #f3d27a;
    --paper-text: #f2ece6;
  }
  * { box-sizing: border-box; margin: 0; padding: 0; }
  html, body { width: 1200px; height: 1063px; overflow: hidden; }
  body {
    background: var(--stage);
    font-family: "Montserrat", sans-serif;
    position: relative;
  }
  .cover {
    position: absolute;
    top: 128px;
    width: 570px;
    height: 806px;
    overflow: hidden;
  }
  .cover--back { left: 30px; }
  .cover--front { left: 600px; }
  .tartan-backdrop {
    position: absolute; inset: 0;
    background:
      linear-gradient(90deg, rgba(20,8,8,.85) 0%, rgba(20,8,8,0) 12%, rgba(20,8,8,0) 88%, rgba(20,8,8,.85) 100%),
      linear-gradient(180deg, rgba(30,10,10,.6) 0%, rgba(30,10,10,0) 20%, rgba(30,10,10,0) 80%, rgba(30,10,10,.6) 100%),
      linear-gradient(100deg, var(--tartan-red) 0%, var(--tartan-green) 18%, var(--tartan-bright) 34%, var(--tartan-red) 52%, var(--tartan-green) 68%, var(--tartan-bright) 84%, var(--tartan-deep) 100%);
  }
  .back-note {
    position: absolute; left: 0; right: 0;
    text-align: center;
    font-weight: 300;
    font-size: 16.5px;
    line-height: 22px;
    color: var(--paper-text);
    text-transform: uppercase;
    letter-spacing: .2px;
  }
  .back-note--top { top: 50px; }
  .back-note--bottom { top: 720px; }
  .bagpipe-art {
    position: absolute;
    left: 150px; top: 150px;
    width: 290px; height: 540px;
    border-radius: 40% 40% 45% 45%;
    background: radial-gradient(ellipse at 55% 65%, #d42a30 0%, #9c1b20 45%, rgba(60,15,15,.0) 75%),
                linear-gradient(180deg, rgba(20,20,20,.6) 0%, rgba(20,20,20,0) 60%);
  }
  .motto {
    position: absolute; left: 47px; top: 98px;
    list-style: none;
  }
  .motto__item {
    display: flex; align-items: center;
    height: 116px; margin-bottom: 51px;
  }
  .motto__icon {
    width: 116px; height: 116px;
    border: 3px solid var(--gold);
    display: flex; align-items: center; justify-content: center;
    flex-shrink: 0;
  }
  .motto__icon svg { width: 74px; height: 74px; stroke: var(--gold); fill: none; stroke-width: 3; stroke-linecap: round; stroke-linejoin: round; }
  .motto__word {
    margin-left: 16px;
    font-family: "Bebas Neue", sans-serif;
    font-size: 74px;
    line-height: 1;
    color: #fff;
    padding-top: 8px;
  }
  .byline {
    position: absolute;
    bottom: 38px;
    writing-mode: vertical-rl;
    transform: rotate(180deg);
    white-space: nowrap;
    text-transform: uppercase;
  }
  .byline__subtitle {
    left: 412px;
    font-weight: 400;
    font-size: 27px;
    color: #fff;
    letter-spacing: .5px;
  }
  .byline__author {
    left: 450px;
    font-weight: 800;
    font-size: 96px;
    line-height: 1;
    letter-spacing: 2px;
    background: linear-gradient(90deg, var(--gold-dark), var(--gold-light) 55%, var(--gold));
    -webkit-background-clip: text; background-clip: text;
    color: transparent;
  }
</style>
</head>
<body>
  <section class="cover cover--back">
    <div class="tartan-backdrop" role="img" aria-label="Soft-focus red tartan fabric background"></div>
    <p class="back-note back-note--top">The real set of bagpipes give an idea of<br>the correct finer details</p>
    <div class="bagpipe-art" role="img" aria-label="Illustration of a set of bagpipes with a red tartan bag and black drones"></div>
    <p class="back-note back-note--bottom">The toy bagpipes perhaps have a better<br>shape with the left 'stick' down</p>
  </section>

  <section class="cover cover--front">
    <div class="tartan-backdrop" role="img" aria-label="Soft-focus red tartan fabric background"></div>
    <ul class="motto">
      <li class="motto__item">
        <span class="motto__icon"><svg viewBox="0 0 74 74"><path d="M14 10 L60 62"/><path d="M8 16 L20 4 M12 20 L24 8 M16 24 L28 12"/><ellipse cx="54" cy="16" rx="8" ry="11" transform="rotate(45 54 16)"/><path d="M48 22 L12 62"/></svg></span>
        <span class="motto__word">Wake</span>
      </li>
      <li class="motto__item">
        <span class="motto__icon"><svg viewBox="0 0 74 74"><path d="M10 12 V62 M10 50 H64 V62 M10 42 H64 V50"/><rect x="16" y="30" width="14" height="10" rx="3"/><path d="M32 40 V34 H60 V42"/></svg></span>
        <span class="motto__word">Stroll</span>
      </li>
      <li class="motto__item">
        <span class="motto__icon"><svg viewBox="0 0 74 74"><path d="M28 54 V16 L56 10 V48"/><ellipse cx="22" cy="54" rx="7" ry="5"/><ellipse cx="50" cy="48" rx="7" ry="5"/></svg></span>
        <span class="motto__word">Hum</span>
      </li>
      <li class="motto__item">
        <span class="motto__icon"><svg viewBox="0 0 74 74"><path d="M18 40 A20 20 0 0 1 52 22"/><path d="M44 20 L53 22 L54 12"/><path d="M56 34 A20 20 0 0 1 22 52"/><path d="M30 54 L21 52 L20 62"/></svg></span>
        <span class="motto__word">Again</span>
      </li>
    </ul>
    <p class="byline byline__subtitle">Music for the bagpipes</p>
    <h1 class="byline byline__author">Dara Colby</h1>
  </section>
</body>
</html>
```